I just need to get that same logo on the business card but with different word. “Marlow Tow and Lease”

Name: Dale K
Number: 4752869014
Email: marlowtow@fennmail.test

On the back, can we di just the logo and marlow tow and lease around it.

If possible a black card with the gold storefront type font that you used before, would be amazing. I attached the original logo just in case.

Target Market(s)

Roadside assistance

Industry/Entity Type

Repair/ roadside

Contact Information for Business Card

Name, email, phone number

Requirements
Must have
• Everything in description
Nice to have
• Nice big logo

```html
<!DOCTYPE html>
<html lang="en">
<head>
<meta charset="utf-8">
<title>Marlow Tow and Lease — Business Card</title>
<link rel="stylesheet" href="https://fonts.googleapis.com/css2?family=Montserrat:wght@400;500;700&display=swap">
<style>
  :root {
    --backdrop: #3a3a3c;
    --card: #1f1f20;
    --gold: #c9a15e;
    --white: #f2f2f2;
    --mark-shade: #2b2b2c;
  }
  html, body {
    margin: 0;
    padding: 0;
    width: 1200px;
    height: 801px;
    overflow: hidden;
    background: var(--backdrop);
    font-family: "Montserrat", Arial, sans-serif;
  }
  .canvas {
    position: relative;
    width: 1200px;
    height: 801px;
  }
  .card {
    position: absolute;
    top: 246px;
    width: 530px;
    height: 303px;
    background: var(--card);
    box-shadow: 0 10px 28px rgba(0,0,0,0.45);
    box-sizing: border-box;
  }
  .card--back { left: 45px; }
  .card--front { left: 625px; }

  /* Back side: brand lockup centred */
  .card--back .lockup {
    position: absolute;
    inset: 0;
    display: flex;
    flex-direction: column;
    align-items: center;
    justify-content: center;
    gap: 18px;
  }
  .brand-square {
    width: 46px;
    height: 46px;
    background: var(--gold);
  }
  .brand-name {
    margin: 0;
    color: var(--gold);
    font-weight: 700;
    text-transform: uppercase;
    letter-spacing: 1px;
    line-height: 1.05;
  }
  .card--back .brand-name {
    font-size: 34px;
    text-align: center;
  }

  /* Front side */
  .card--front .brand-name {
    position: absolute;
    left: 46px;
    top: 96px;
    font-size: 32px;
  }
  .mark-panel {
    position: absolute;
    right: 50px;
    top: 34px;
    width: 118px;
    height: 118px;
    background: var(--mark-shade);
  }
  .contact {
    position: absolute;
    left: 110px;
    top: 176px;
    color: var(--white);
  }
  .contact .person-name {
    margin: 0;
    color: var(--gold);
    font-weight: 700;
    font-size: 19px;
    letter-spacing: 1px;
    text-transform: uppercase;
  }
  .contact .person-role {
    margin: 2px 0 8px;
    font-size: 13px;
    font-weight: 500;
  }
  .contact .rule {
    width: 150px;
    height: 1.5px;
    background: var(--gold);
    margin-bottom: 10px;
  }
  .contact-line {
    display: flex;
    align-items: center;
    gap: 8px;
    font-size: 14px;
    margin-bottom: 6px;
  }
  .contact-line svg { flex: none; }
</style>
</head>
<body>
<main class="canvas">

  <section class="card card--back" aria-label="Card back">
    <div class="lockup">
      <div class="brand-square" aria-hidden="true"></div>
      <p class="brand-name">Marlow Tow<br>and Lease</p>
    </div>
  </section>

  <section class="card card--front" aria-label="Card front">
    <div class="mark-panel" aria-hidden="true"></div>
    <p class="brand-name">Marlow Tow<br>and Lease</p>

    <div class="contact">
      <p class="person-name">Dale K</p>
      <p class="person-role">President</p>
      <div class="rule"></div>
      <div class="contact-line">
        <svg width="12" height="12" viewBox="0 0 24 24" aria-hidden="true">
          <path fill="var(--gold)" d="M6.6 10.8a15.1 15.1 0 0 0 6.6 6.6l2.2-2.2a1 1 0 0 1 1-.25 11.4 11.4 0 0 0 3.6.57 1 1 0 0 1 1 1V20a1 1 0 0 1-1 1A17 17 0 0 1 3 4a1 1 0 0 1 1-1h3.5a1 1 0 0 1 1 1c0 1.25.2 2.45.57 3.57a1 1 0 0 1-.25 1z"/>
        </svg>
        <span>4752869014</span>
      </div>
      <div class="contact-line">
        <svg width="13" height="10" viewBox="0 0 26 20" aria-hidden="true">
          <rect x="0" y="0" width="26" height="20" rx="2" fill="var(--gold)"/>
          <path d="M1 2 L13 11 L25 2" fill="none" stroke="var(--card)" stroke-width="2"/>
        </svg>
        <span>marlowtow@fennmail.test</span>
      </div>
    </div>
  </section>

</main>
</body>
</html>
```